Dental Plan for Dogs

We are a vet clinic and I am wanting a poster designed that can then ultimately be changed/rejigged to be use on a website/facebook as a banner ad that promotes dental health in dogs. Therefore I will need the photoshop files as well as pngs/pdfs.
I want a dog and a cat in the image used for the poster with them showing healthy teeth and looking happy!
The feels is to be professional but also cute/funny. Using the orange coming through from the logo and the logo somewhere on the poster.
The text as below
Heading: Join our Dental Bluebell Plan!
Text: Keep your fur child smiling all year round while we cap their dental work at $365 if they return for a dental clean within 365 days! The plan includes full mouth dental x-rays and scale and polish of all teeth under a carefully monitored general anaesthetic! That'll give you both a reason to smile and save you over $180 per dental! *
Conditions (in smaller writing): *Any extractions and more advanced dental procedures if required will incur an additional cost that will be discussed with your prior to the procedure.
Thanks

```html
<!DOCTYPE html>
<html lang="en">
<head>
<meta charset="utf-8">
<title>Join our Dental Bluebell Plan</title>
<link href="https://fonts.googleapis.com/css2?family=Dancing+Script:wght@500&family=Lilita+One&family=Arimo:wght@400;700&display=swap" rel="stylesheet">
<style>
  :root {
    --brown: #5b3d2c;
    --orange: #f29a1f;
    --text: #5a5a5a;
    --bg-light: #ffffff;
    --bg-soft: #ecebea;
    --fur-tan: #c8a27a;
    --fur-dark: #8a6a52;
  }
  * { margin: 0; padding: 0; box-sizing: border-box; }
  html, body { width: 1200px; height: 444px; overflow: hidden; }
  body {
    position: relative;
    background: radial-gradient(ellipse at 35% 45%, var(--bg-light) 0%, var(--bg-light) 45%, var(--bg-soft) 100%);
    font-family: "Arimo", Arial, sans-serif;
    color: var(--text);
  }
  .banner { position: absolute; inset: 0; }
  .pets-photo {
    position: absolute;
    left: 600px; top: 50px;
    width: 600px; height: 345px;
    background: radial-gradient(ellipse at 60% 55%, var(--fur-tan) 0%, var(--fur-dark) 45%, rgba(236,235,234,0) 75%);
  }
  .eyebrow {
    position: absolute;
    left: 54px; top: 48px;
    font-family: "Dancing Script", cursive;
    font-weight: 500;
    font-size: 74px;
    line-height: 1;
    color: var(--brown);
  }
  .headline {
    position: absolute;
    left: 56px; top: 140px;
    font-family: "Lilita One", sans-serif;
    font-size: 60px;
    line-height: 1;
    letter-spacing: 1px;
    color: var(--brown);
    text-transform: uppercase;
    white-space: nowrap;
  }
  .headline .accent { color: var(--orange); }
  .intro {
    position: absolute;
    left: 56px; top: 250px;
    width: 700px;
    font-size: 17px;
    line-height: 21px;
    color: var(--text);
  }
  .intro .saving {
    color: var(--orange);
    font-weight: 700;
    font-size: 21px;
  }
  .conditions {
    position: absolute;
    left: 748px; top: 398px;
    width: 440px;
    font-size: 10.5px;
    line-height: 14px;
    color: var(--text);
  }
  .clinic-mark {
    position: absolute;
    right: 22px; top: 30px;
    display: flex;
    align-items: center;
    gap: 8px;
    font-family: "Lilita One", sans-serif;
    font-size: 26px;
    color: var(--orange);
  }
  .clinic-mark .dot {
    width: 22px; height: 22px;
    border-radius: 50%;
    background: var(--orange);
  }
  .clinic-mark .place { display: block; font-size: 26px; }
</style>
</head>
<body>
  <main class="banner">
    <div class="pets-photo" role="img" aria-label="A happy ginger kitten sitting beside a smiling brown bulldog lying down with its tongue out, with small red hearts floating above"></div>

    <p class="eyebrow">Join our</p>
    <h1 class="headline">Dental <span class="accent">Bluebell</span> Plan!</h1>

    <p class="intro">Keep your fur child smiling all year round while we cap their dental work at $365 if they return for a dental clean within 365 days! The plan includes full mouth dental x-rays and scale and polish of all teeth under a carefully monitored general anaesthetic! That'll give you both a reason to smile and save you over <span class="saving">$180 per dental!</span> *</p>

    <div class="clinic-mark">
      <span class="dot"></span>
      <span>Tailwag Vet Clinic<span class="place">Elm Grove</span></span>
    </div>

    <p class="conditions">*Any extractions and more advanced dental procedures if required will incur an additional cost that will be discussed with your prior to the procedure.</p>
  </main>
</body>
</html>
```